依頼詳細
下記ブランドコンセプトに沿ったご提案をお願い致します。
プロトタイプを添付いたします。構成等、より優れていると思えるご提案がありましたら無視して頂いて構いません。
ブランドコンセプトは以下の通りです。

-- 以下、ブランドコンセプト
「自然が持つ美しさ」と「暮らす人の思い」を取り入れ『生活が楽しい住まい』を創ります
人々に永く愛されてきた天然素材を使用することで自然素材だけが持つ色や質感から確かな手触りと温もりを暮らす人に与え続けてくれます。新しいだけを追い過ぎず自然素材の持つ機能性を生かして自然の働きでしっかりと家を守る
それは流行に左右されない気品を保つ「素朴で美しい風合い」に仕上がります。

住む人のライフスタイルや好みをしっかりとお聞かせいただいた上で土地を生かし隣地環境と調和のある設計を企画し、その人らしい家を一緒に考えていきます。
それはその人がどんなふうに暮らしていきたいのかを一緒に考え、その地で永く暮らしていくイメージを膨らませ生活が楽しくなる様な空間を提案します。
-- 以上、ブランドコンセプト
サイトURL
http://tovaru.com/
ページ数
1ページ
希望イメージ
シンプル 複雑
単色 カラフル
暗い 明るい
日常 高級
遊び心 厳粛
未来的 伝統的
女性的 男性的
希望する色
納品ファイル
補足説明
トップページに関するプロトタイプを「トップページ.png」として添付しております。
また、素材として利用可能なものは下記dropboxリンクよりご利用ください。
https://www.filoshare-box.net/s/7kq2mz/sample-assets

■ 選んだ理由

全員が色使いやコンテンツの配置などを理由として同デザインを選択しました。
似通ったデザインの中でも全員の目を引く、魅力的な部分があったのだと考えます。

■ 提案者全員のお礼・コメント

今回は多くの皆様に貴重なお時間を使って頂きご提案頂きました事、大変うれしく思い感謝申し上げます。
複数名で選考を行いましたが、選考するメンバー全員でどれも素晴らしいデザインだよねと口をそろえて申しておりました。

本当にありがとうございました。

```html
<!DOCTYPE html>
<html lang="ja">
<head>
<meta charset="utf-8">
<title>Tovaru | 自然素材の家づくり</title>
<link href="https://fonts.googleapis.com/css2?family=Noto+Sans+JP:wght@400;500;700&family=Noto+Serif+JP:wght@500;700&family=Lato:wght@400;700&display=swap" rel="stylesheet">
<style>
:root{
  --green:#9cb82a;
  --green-dark:#7f9a17;
  --green-pale:#eef3d8;
  --ink:#3b3b3b;
  --muted:#8a8a8a;
  --line:#dcdcdc;
  --paper:#ffffff;
  --bg:#f5f5f0;
  --footer:#2e2e2e;
  --footer-line:#444;
}
*{box-sizing:border-box;margin:0;padding:0}
html,body{width:1200px;height:2800px;overflow:hidden}
body{background:var(--paper);color:var(--ink);font-family:"Noto Sans JP",sans-serif;font-size:14px;line-height:1.7}
.wrap{width:960px;margin:0 auto;position:relative}

/* header */
.site-header{height:150px;border-top:6px solid var(--green)}
.site-header .wrap{height:100%}
.brand{position:absolute;left:0;top:18px;display:flex;align-items:center;gap:12px}
.brand-mark{width:34px;height:34px;background:var(--green)}
.brand-name{font-family:"Lato",sans-serif;font-weight:700;font-size:30px;color:var(--green-dark);letter-spacing:.04em}
.tagline{position:absolute;left:0;top:0;font-size:11px;color:var(--muted)}
.tel{position:absolute;right:0;top:14px;text-align:right}
.tel-number{font-family:"Noto Serif JP",serif;font-size:26px;color:var(--green-dark);font-weight:700}
.btn{display:inline-block;background:var(--green);color:#fff;font-size:12px;padding:4px 16px;border-radius:2px}
.global-nav{position:absolute;left:0;right:0;bottom:12px;display:flex;border-left:1px solid var(--line)}
.global-nav a{flex:1;text-align:center;border-right:1px solid var(--line);padding:4px 0;text-decoration:none;color:var(--ink);font-size:14px;font-weight:500;line-height:1.4}
.global-nav small{display:block;font-family:"Lato",sans-serif;font-size:10px;color:var(--green);letter-spacing:.1em}

/* hero */
.hero{height:440px;position:relative;background:linear-gradient(180deg,#c9d9ea 0%,#e4ecf2 38%,#d8d4cc 60%,#9a9284 85%,#7b8360 100%)}
.hero-copy{position:absolute;right:130px;top:70px;width:440px;background:rgba(255,255,255,.82);border:1px solid var(--green);padding:16px 20px;text-align:center;font-family:"Noto Serif JP",serif}
.hero-copy p{font-size:14px;color:var(--ink)}
.hero-copy strong{display:block;font-size:24px;color:var(--green-dark);margin-top:4px;font-weight:700}

/* content grid */
.content{display:flex;gap:30px;margin-top:40px}
.main{width:700px}
.side{width:230px}
.section-title{font-family:"Noto Serif JP",serif;font-size:20px;font-weight:700;border-bottom:2px solid var(--line);padding-bottom:6px;margin-bottom:22px;position:relative}
.section-title::after{content:"";position:absolute;left:0;bottom:-2px;width:120px;height:2px;background:var(--green)}
.section-title small{font-family:"Lato",sans-serif;font-size:12px;color:var(--green);font-weight:400;margin-left:10px}
.section-title .more{position:absolute;right:0;bottom:8px;font-family:"Noto Sans JP",sans-serif;font-size:12px;font-weight:400;color:var(--ink)}

.concept-images{display:flex;justify-content:space-between;padding:0 40px;margin-bottom:26px}
.concept-circle{width:170px;height:170px;border-radius:50%;border:5px solid var(--green-pale)}
.concept-circle.leaves{background:linear-gradient(135deg,#a8c95a,#5f8a2c)}
.concept-circle.hands{background:linear-gradient(135deg,#e6d0b8,#b78e6c)}
.concept-circle.sprout{background:linear-gradient(135deg,#cfe08a,#6d9a34)}
.concept-text p{font-size:13px;line-height:2;margin-bottom:10px}

.pair{display:flex;gap:20px;margin-top:30px}
.card{flex:1;border:1px solid var(--line);height:190px;position:relative;padding:16px}
.card-title{font-family:"Noto Serif JP",serif;font-size:17px;font-weight:700;text-align:center}
.card-title small{display:block;font-family:"Lato",sans-serif;font-size:11px;color:var(--green);font-weight:400;letter-spacing:.1em}
.card.home{display:flex;gap:14px;align-items:center}
.card.home .thumb{width:150px;height:150px;background:linear-gradient(160deg,#dfe6ee,#a59b8b)}
.card.home .card-title{flex:1}
.card.contact{text-align:center;background:var(--green-pale)}
.card.contact .tel-number{display:block;margin:10px 0 8px}

.news{margin-top:46px}
.news-item{display:flex;gap:20px;padding:16px 0;border-bottom:1px dotted var(--line);height:126px}
.news-thumb{width:150px;height:94px;flex:none;background:linear-gradient(170deg,#cdd9e6,#e7e6df 50%,#8f8a74)}
.news-body{flex:1;position:relative}
.news-date{font-family:"Lato",sans-serif;font-size:12px;color:var(--muted);margin-right:12px}
.news-head{font-size:14px;color:var(--green-dark);font-weight:500;border-bottom:1px solid var(--green)}
.news-body p{font-size:12px;color:var(--ink);margin-top:6px}
.news-body .btn{position:absolute;right:0;bottom:0;font-size:11px}

.works{border:1px solid var(--line);padding:14px}
.works .section-title{font-size:17px;margin-bottom:14px}
.works .section-title::after{width:60px}
.work{margin-bottom:16px}
.work-photo{height:170px;background:linear-gradient(170deg,#c8d7e6,#e8e6e0 45%,#9b907c)}
.work-cap{font-size:11px;color:var(--muted);margin-top:4px}
.works .btn{display:block;text-align:center}

.page-top{margin-top:40px;text-align:center;font-family:"Lato",sans-serif;font-size:11px;letter-spacing:.1em;color:var(--muted);height:40px}

/* footer */
.site-footer{background:var(--footer);height:730px;padding-top:40px;color:#ccc}
.sns-box{width:640px;margin:0 auto;background:#fff;height:390px;padding:12px;color:var(--ink)}
.sns-head{font-size:13px;font-weight:700;border-bottom:1px solid var(--line);padding-bottom:6px}
.sns-cover{height:110px;margin-top:10px;background:linear-gradient(170deg,#cdd9e6,#dad7cf 55%,#8c8570)}
.sns-meta{font-size:12px;padding:8px 0;border-bottom:1px solid var(--line)}
.sns-meta b{color:var(--green-dark)}
.sns-fans{height:170px;margin-top:12px;background:linear-gradient(90deg,#bfbfbf,#d6d6d6,#bfbfbf)}
.footer-nav{width:960px;margin:36px auto 0;display:flex;gap:0;border-top:1px solid var(--footer-line);border-bottom:1px solid var(--footer-line);padding:12px 0}
.footer-nav a{color:#ccc;font-size:12px;text-decoration:none;padding:0 18px;border-right:1px solid var(--footer-line)}
.footer-info{width:960px;margin:28px auto 0;display:flex;align-items:flex-start;gap:16px}
.footer-info .brand-mark{width:26px;height:26px}
.footer-info .brand-name{font-size:22px;color:#fff;line-height:1}
.footer-info address{font-style:normal;font-size:11px;line-height:1.8;color:#aaa;margin-left:24px}
.copyright{width:960px;margin:34px auto 0;text-align:right;font-family:"Lato",sans-serif;font-size:11px;color:#888}
</style>
</head>
<body>

<header class="site-header">
  <div class="wrap">
    <p class="tagline">tovaru | 自然素材の家づくりなら</p>
    <div class="brand"><span class="brand-mark"></span><span class="brand-name">Tovaru</span></div>
    <div class="tel">
      <div class="tel-number">tel.0120-48-3710</div>
      <a class="btn">お問い合わせはこちら</a>
    </div>
    <nav class="global-nav">
      <a>トップ<small>HOME</small></a>
      <a>家づくり<small>CONCEPT</small></a>
      <a>施工事例<small>WORKS</small></a>
      <a>お問い合わせ<small>CONTACT</small></a>
      <a>資料請求<small>REQUEST</small></a>
      <a>会社概要<small>COMPANY</small></a>
    </nav>
  </div>
</header>

<section class="hero" role="img" aria-label="青空の下に建つ白壁と濃い屋根の二階建て住宅の写真">
  <div class="hero-copy">
    <p>「自然が持つ美しさ」と「暮らす人の思い」を取り入れ</p>
    <strong>『生活が楽しい住まい』</strong>
  </div>
</section>

<div class="wrap content">
  <main class="main">
    <section class="concept">
      <h2 class="section-title">トヴァルのブランドコンセプト<small>concept</small></h2>
      <div class="concept-images">
        <div class="concept-circle leaves" role="img" aria-label="若葉と家のかたちの写真"></div>
        <div class="concept-circle hands" role="img" aria-label="手のひらに木の実をのせた写真"></div>
        <div class="concept-circle sprout" role="img" aria-label="手で包んだ新芽の写真"></div>
      </div>
      <div class="concept-text">
        <p>「自然が持つ美しさ」と「暮らす人の思い」を取り入れ『生活が楽しい住まい』を創ります。人々に永く愛されてきた天然素材を使用することで自然素材だけが持つ色や質感から確かな手触りと温もりを暮らす人に与え続けてくれます。新しいだけを追い過ぎず自然素材の持つ機能性を生かして自然の働きでしっかりと家を守る。それは流行に左右されない気品を保つ「素朴で美しい風合い」に仕上がります。</p>
        <p>住む人のライフスタイルや好みをしっかりとお聞かせいただいた上で土地を生かし隣地環境と調和のある設計を企画し、その人らしい家を一緒に考えていきます。それはその人がどんなふうに暮らしていきたいのかを一緒に考え、その地で永く暮らしていくイメージを膨らませ生活が楽しくなる様な空間を提案します。</p>
      </div>
    </section>

    <div class="pair">
      <div class="card home">
        <div class="card-title">トヴァルの家づくり<small>CONCEPT</small></div>
        <div class="thumb" role="img" aria-label="施工した住宅の外観写真"></div>
      </div>
      <div class="card contact">
        <div class="card-title">お気軽にご相談下さい。<small>CONTACT</small></div>
        <span class="tel-number">tel.0120-48-3710</span>
        <a class="btn">お問い合わせフォームはこちら</a>
      </div>
    </div>

    <section class="news">
      <h2 class="section-title">最新情報<small>Latest news</small><span class="more">一覧を見る ›</span></h2>
      <article class="news-item">
        <div class="news-thumb" role="img" aria-label="住宅外観の写真"></div>
        <div class="news-body">
          <div class="news-head"><span class="news-date">2014.11.18</span>ホームページをリニューアルしました。</div>
          <p>新しいサイトでは施工事例や家づくりの考え方をわかりやすくご紹介しています。ぜひご覧ください。</p>
          <a class="btn">続きを見る</a>
        </div>
      </article>
      <article class="news-item">
        <div class="news-thumb" role="img" aria-label="住宅外観の写真"></div>
        <div class="news-body">
          <div class="news-head"><span class="news-date">2014.11.18</span>ホームページをリニューアルしました。</div>
          <p>新しいサイトでは施工事例や家づくりの考え方をわかりやすくご紹介しています。ぜひご覧ください。</p>
          <a class="btn">続きを見る</a>
        </div>
      </article>
      <article class="news-item">
        <div class="news-thumb" role="img" aria-label="住宅外観の写真"></div>
        <div class="news-body">
          <div class="news-head"><span class="news-date">2014.11.18</span>ホームページをリニューアルしました。</div>
          <p>新しいサイトでは施工事例や家づくりの考え方をわかりやすくご紹介しています。ぜひご覧ください。</p>
          <a class="btn">続きを見る</a>
        </div>
      </article>
    </section>
  </main>

  <aside class="side">
    <section class="works">
      <h2 class="section-title">施工事例<small>works</small></h2>
      <div class="work"><div class="work-photo" role="img" aria-label="施工事例の住宅外観写真"></div><p class="work-cap">施工事例 01 / 伊那市</p></div>
      <div class="work"><div class="work-photo" role="img" aria-label="施工事例の住宅外観写真"></div><p class="work-cap">施工事例 02 / 駒ヶ根市</p></div>
      <div class="work"><div class="work-photo" role="img" aria-label="施工事例の住宅外観写真"></div><p class="work-cap">施工事例 03 / 飯田市</p></div>
      <a class="btn">施工事例をもっと見る</a>
    </section>
  </aside>
</div>

<div class="page-top">PAGE TOP</div>

<footer class="site-footer">
  <div class="sns-box">
    <div class="sns-head">SNSのページ</div>
    <div class="sns-cover" role="img" aria-label="住宅外観のカバー写真"></div>
    <div class="sns-meta"><b>Tovaru</b>　ほか120人が「いいね！」しています</div>
    <div class="sns-fans" role="img" aria-label="フォロワーのアイコン一覧"></div>
  </div>
  <nav class="footer-nav">
    <a>トップページ</a><a>家づくり</a><a>施工事例</a><a>お問い合わせ</a><a>資料請求</a><a>会社概要</a>
  </nav>
  <div class="footer-info">
    <span class="brand-mark"></span><span class="brand-name">Tovaru</span>
    <address>株式会社トヴァル<br>長野県上伊那郡みどり町1-2-3<br>TEL 0120-48-3710</address>
  </div>
  <p class="copyright">Copyright (C) TOVARU CORPORATION All Rights Reserved.</p>
</footer>

</body>
</html>
```